Attract customers for New Zealand forest eco tour

Website design for a new eco tourism business in New Zealand. We have domain name booked for it: www.GlenofTavi.co.nz

We have written the site, see attachments. And have all the pictures to go with it, have just attached a few of these for examples. Will provide the rest to the winning bidder.

We want the look of the site to be highly visually attractive, clean and uncluttered. And if you know about what works best for eco-tourism, that will help.

Website should be mobile phone readable, as well as desktop.

Our objectives for the site are to introduce our forest to them, get people interested in visiting, and have people book trips. We will need some kind of booking app such as with dates of bookings, and ideally a payment app as well so they can pay for bookings.

Ideally, I don't know if you can do this, you use a format which allows us to self edit the site (note, we're not technical experts).

Target Market(s)

Professional people aged 30 - 49.
Looking to travel, probably as a couple.
International travel for adventure, relaxation.

Key things they want are:

See attractions
Go to a place different from their own country
Escape from their usual working life
Unwind and relax

Industry/Entity Type

Business

Coding

Coded - Design and coding required

Number of Pages Required

5+ page

Colors
9bcb3b

Requirements
Must have
• Visually attractive - pictorial look
• Clean and uncluttered - blank space
• Mobile readable and desktop
• Booking app
• Payment app
Nice to have
• Be self editable by us (non-technical people)
Should not have
• shouldn't look cheap

```html
<!DOCTYPE html>
<html lang="en">
<head>
<meta charset="utf-8">
<title>Glen of Tavi — Forest Eco Tours</title>
<link href="https://fonts.googleapis.com/css2?family=Open+Sans:wght@400;600;700;800&display=swap" rel="stylesheet">
<style>
:root{
  --green:#9bcb3b;
  --green-dark:#86b52c;
  --white:#ffffff;
  --ink:#333333;
  --muted:#6b6b6b;
  --pale:#eef0ea;
  --forest-deep:#1f2a16;
  --forest-mid:#3f5a26;
  --sky:#5d6f86;
  --night:#161b22;
  --footer-bg:#e4e5e1;
}
*{margin:0;padding:0;box-sizing:border-box}
html,body{width:1200px;height:2376px;overflow:hidden}
body{font-family:"Open Sans",Arial,sans-serif;color:var(--ink);background:var(--white);position:relative}
.site-header{position:absolute;left:0;top:0;width:1200px;height:480px}
.hero-photo{position:absolute;inset:0;background:radial-gradient(ellipse at 50% 55%,#6d6a4f 0%,#3d4a25 35%,#26361a 70%,#1a2512 100%)}
.brand{position:absolute;left:100px;top:14px;width:80px;color:var(--white);font-weight:800;font-size:15px;line-height:17px;text-transform:uppercase;text-align:center}
.search{position:absolute;right:100px;top:46px;width:170px;height:24px;background:var(--white);border:1px solid #ccc;font-size:12px;color:#888;padding:4px 8px}
.main-nav{position:absolute;left:100px;top:100px;width:1000px;height:40px;background:var(--green);display:flex;align-items:center;padding:0 14px}
.main-nav a{color:var(--white);text-decoration:none;font-size:13px;font-weight:700;margin-right:30px}
.social{margin-left:auto;display:flex;gap:8px}
.social span{width:26px;height:26px;border-radius:50%;border:2px solid var(--white)}
.slider-dots{position:absolute;left:0;right:0;top:446px;display:flex;justify-content:center;gap:8px}
.slider-dots span{width:10px;height:10px;border-radius:50%;background:rgba(255,255,255,.55)}
.slider-dots span.active{background:var(--white)}

.why{position:absolute;left:0;top:480px;width:1200px;height:540px;background:var(--pale)}
.section-title{text-align:center;font-size:28px;font-weight:800;color:#3a3a3a;padding-top:24px;letter-spacing:.5px}
.section-title::after{content:"";display:block;width:300px;height:1px;background:#bbb;margin:10px auto 0}
.reasons{position:absolute;left:88px;top:80px;width:1024px;display:flex;justify-content:space-between}
.reason{width:290px}
.reason h3{color:var(--green);font-size:22px;font-weight:700;line-height:24px}
.reason p{font-size:12px;color:var(--muted);font-weight:600;text-transform:uppercase;margin-top:8px;line-height:15px}
.gallery{position:absolute;left:88px;top:210px;width:1024px;height:300px;display:grid;grid-template-columns:332px 332px 348px;grid-template-rows:148px 148px;gap:4px 6px}
.tile{position:relative;display:flex;align-items:center;justify-content:center}
.tile .label{position:relative;color:var(--white);font-weight:700;font-size:16px;letter-spacing:.5px}
.tile.tall{grid-column:3;grid-row:1 / span 2}
.tile.a{background:linear-gradient(160deg,#4a5a44,#2c3a2e)}
.tile.b{background:linear-gradient(160deg,#d6493a,#2f6fa8 70%)}
.tile.c{background:linear-gradient(160deg,#2a9ab0,#0c5a68)}
.tile.d{background:linear-gradient(160deg,#b44a3a,#e7e7e7 80%)}
.tile.e{background:linear-gradient(160deg,#3cb4c8,#1d8a6a)}

.activities{position:absolute;left:0;top:1020px;width:1200px;height:600px}
.landscape{position:absolute;inset:0;background:linear-gradient(180deg,#2a3640 0%,#3b4a3a 22%,#55733a 40%,#c9d3d8 62%,#eef1f2 80%,#f4f5f5 100%)}
.activity-row{position:absolute;left:88px;top:230px;width:1024px;display:flex;justify-content:space-between}
.activity{width:260px;text-align:center}
.activity .ring{width:230px;height:230px;margin:0 auto;border-radius:50%;background:var(--green);border:8px solid var(--white);display:flex;align-items:center;justify-content:center;position:relative}
.activity .ring::after{content:"";position:absolute;bottom:-14px;left:50%;margin-left:-14px;width:28px;height:28px;border-radius:50%;background:var(--white)}
.activity.mid{margin-top:-60px}
.activity p{font-size:11px;color:#555;font-weight:600;text-transform:uppercase;margin-top:24px;line-height:14px}
.btn{display:inline-block;background:var(--green);color:var(--white);font-size:11px;font-weight:700;padding:6px 16px;margin-top:16px;border-radius:2px}

.hikes{position:absolute;left:0;top:1620px;width:1200px;height:240px;background:linear-gradient(180deg,#1d2a35,#2c4350 55%,#4e7488)}
.hike-row{position:absolute;left:88px;top:52px;width:1024px;display:flex;justify-content:space-between}
.hike{width:230px;color:var(--white)}
.hike h4{font-size:17px;font-weight:700}
.hike p{font-size:11px;line-height:15px;margin-top:10px;color:#dfe6ea}

.quote{position:absolute;left:0;top:1920px;width:1200px;height:200px;background:linear-gradient(180deg,#2a1d1a,#3a2620 60%,#201612)}
.quote-mark{position:absolute;left:212px;top:40px;color:var(--white);font-size:70px;font-weight:800;line-height:60px}
.quote p{position:absolute;left:250px;top:58px;width:720px;color:var(--white);font-size:13px;line-height:19px;font-style:normal}

.site-footer{position:absolute;left:0;top:2140px;width:1200px;height:236px;background:var(--footer-bg)}
.footer-cols{position:absolute;left:88px;top:32px;width:1024px;display:flex}
.footer-col{width:256px;padding-left:24px;border-left:1px solid #c4c6bf}
.footer-col:first-child{border-left:none;padding-left:0}
.footer-col h5{font-size:14px;font-weight:700;color:#333;margin-bottom:10px}
.footer-col li{list-style:none;font-size:11px;color:#666;line-height:17px}
.copyright{position:absolute;left:0;bottom:0;width:1200px;height:36px;border-top:1px solid #cfd1cb;text-align:center;font-size:11px;color:#666;line-height:36px}
.copyright a{color:var(--green-dark);text-decoration:none}
</style>
</head>
<body>

<header class="site-header">
  <div class="hero-photo" role="img" aria-label="Photo of a native owl perched among forest leaves"></div>
  <div class="brand">Glen of Tavi</div>
  <div class="search">Search</div>
  <nav class="main-nav">
    <a href="#">Glen Of Tavi</a>
    <a href="#">Tours</a>
    <a href="#">Activities</a>
    <a href="#">Project</a>
    <a href="#">Local Attraction</a>
    <a href="#">Book</a>
    <a href="#">Contact Us</a>
    <div class="social"><span></span><span></span><span></span><span></span></div>
  </nav>
  <div class="slider-dots"><span></span><span class="active"></span><span></span></div>
</header>

<section class="why">
  <h2 class="section-title">WHY CHOOSE US</h2>
  <div class="reasons">
    <div class="reason"><h3>01.<br>CONSECTETUER</h3><p>Praesent justo dolor, lobortis sed augue auctor, dolor lorem ipsum</p></div>
    <div class="reason"><h3>02.<br>CONSECTETUER</h3><p>Praesent justo dolor, lobortis sed augue auctor, dolor lorem ipsum</p></div>
    <div class="reason"><h3>03.<br>CONSECTETUER</h3><p>Praesent justo dolor, lobortis sed augue auctor, dolor lorem ipsum</p></div>
  </div>
  <div class="gallery">
    <div class="tile a" role="img" aria-label="Photo of a forest walking track"><span class="label">PONSECTETUER</span></div>
    <div class="tile b" role="img" aria-label="Photo of a rafting group on a river"><span class="label">PONSECTETUER</span></div>
    <div class="tile tall c" role="img" aria-label="Photo of divers underwater"><span class="label">PONSECTETUER</span></div>
    <div class="tile d" role="img" aria-label="Photo of a kayak trip"><span class="label">PONSECTETUER</span></div>
    <div class="tile e" role="img" aria-label="Photo of a boat on turquoise water"><span class="label">PONSECTETUER</span></div>
  </div>
</section>

<section class="activities">
  <div class="landscape" role="img" aria-label="Photo of green farmland and mountains at dusk"></div>
  <div class="activity-row">
    <div class="activity">
      <div class="ring">
        <svg width="90" height="110" viewBox="0 0 90 110" role="img" aria-label="Hiking pictogram"><rect x="20" y="10" width="50" height="90" rx="25" fill="#ffffff"/></svg>
      </div>
      <p>Praesent justo dolor, lobortis sed augue auctor, dolor lorem ipsum</p>
      <span class="btn">Read More</span>
    </div>
    <div class="activity mid">
      <div class="ring">
        <svg width="100" height="110" viewBox="0 0 100 110" aria-hidden="true">
          <path d="M50 8 C62 30 76 44 70 66 C66 80 58 86 50 86 C42 86 34 80 30 66 C26 50 40 40 50 8Z" fill="#ffffff"/>
          <path d="M50 44 C56 56 60 64 56 74 C54 78 46 78 44 74 C40 64 46 56 50 44Z" fill="#9bcb3b"/>
          <rect x="12" y="90" width="76" height="9" rx="4" fill="#ffffff" transform="rotate(12 50 94)"/>
          <rect x="12" y="90" width="76" height="9" rx="4" fill="#ffffff" transform="rotate(-12 50 94)"/>
        </svg>
      </div>
      <p>Praesent justo dolor, lobortis sed augue auctor, dolor lorem ipsum</p>
      <span class="btn">Read More</span>
    </div>
    <div class="activity">
      <div class="ring">
        <svg width="130" height="100" viewBox="0 0 130 100" aria-hidden="true">
          <path d="M10 90 L50 20 L120 20 L125 90 Z" fill="#ffffff"/>
          <path d="M32 90 L50 52 L68 90 Z" fill="#9bcb3b"/>
        </svg>
      </div>
      <p>Praesent justo dolor, lobortis sed augue auctor, dolor lorem ipsum</p>
      <span class="btn">Read More</span>
    </div>
  </div>
</section>

<section class="hikes">
  <div class="hike-row">
    <div class="hike"><h4>Take a Hike</h4><p>Praesent justo dolor, lobortis sed augue auctor, dolor lorem ipsum nunc.</p><span class="btn">Read More</span></div>
    <div class="hike"><h4>Take a Hike</h4><p>Praesent justo dolor, lobortis sed augue auctor, dolor lorem ipsum nunc.</p><span class="btn">Read More</span></div>
    <div class="hike"><h4>Take a Hike</h4><p>Praesent justo dolor, lobortis sed augue auctor, dolor lorem ipsum nunc.</p><span class="btn">Read More</span></div>
    <div class="hike"><h4>Take a Hike</h4><p>Praesent justo dolor, lobortis sed augue auctor, dolor lorem ipsum nunc.</p><span class="btn">Read More</span></div>
  </div>
</section>

<section class="quote" aria-label="Visitor quote">
  <span class="quote-mark">&ldquo;</span>
  <p>Lorem ipsum dolor sit amet, consectetuer adipiscing elit. Aenean commodo ligula eget dolor. Aenean massa. Cum sociis natoque penatibus et magnis dis parturient montes, nascetur ridiculus mus. Donec quam felis, ultricies nec, pellentesque eu, pretium quis, sem. Nulla consequat massa quis enim. Donec pede justo, fringilla vel, aliquet nec.</p>
</section>

<footer class="site-footer">
  <div class="footer-cols">
    <div class="footer-col"><h5>About</h5><ul><li>About Us</li><li>Blog</li><li>Contact Us</li><li>Site Map</li><li>Privacy</li></ul></div>
    <div class="footer-col"><h5>Your Policy</h5><ul><li>Help &amp; Assistance</li><li>Cancel your order</li><li>Cancel your policy</li><li>How to claim</li><li>FAQ</li></ul></div>
    <div class="footer-col"><h5>Planning Your Trip</h5><ul><li>Native Birds</li><li>Map</li><li>Weather</li><li>Getting There</li><li>FAQ</li></ul></div>
    <div class="footer-col"><h5>Travel Insurance</h5><ul><li>Complete cover</li><li>Extra cover</li><li>Bank and liaise</li><li>Account info</li><li>Travel plans</li></ul></div>
  </div>
  <div class="copyright">Copyright &copy; 2014 All Rights Reserved &nbsp;|&nbsp; <a href="#">Privacy Policy</a></div>
</footer>

</body>
</html>
```